Occupational Therapist does home accessibility for disabled folks; needs business card design

We need a business card for a company in Portland, Oregon that specializes in making homes accessible, comfortable, and functional for people who are disabled or aging who would like to stay in THEIR home. Our medical background as Occupational Therapists allows us to translate the functional needs of the person into the recommendations for the design of the home remodel.

Target Market(s)

Elderly, children of elderly
People with disabilities, families of people with disabilities

Industry/Entity Type

Business

Contact Information for Business Card

Company name: HomeWise
Name: Danielle Reyes Crawford, OTR/L, CAPS, ECHM
Occupational Therapist, Home Modification & Accessibility Specialist
website: www.homewiseforyears.com
email: homewiseforyears@nestmail.example
phone: (503)218-4057
CCB #: 487315

Font styles to use
Sans Serif

Requirements
Must have
• My logo
• Easy to read font with contrasting background
• Please list the Services offered: Occupational Therapy, Home safety & accessibility assessments, Home modification consulting, project management
Nice to have
• Friendly, welcoming feel
Should not have
• Dark colored background

```html
<!DOCTYPE html>
<html lang="en">
<head>
<meta charset="utf-8">
<title>HomeWise Business Card</title>
<link rel="stylesheet" href="https://fonts.googleapis.com/css2?family=Roboto+Condensed:wght@400&display=swap">
<style>
  :root {
    --brand-orange: #d0802b;
    --ornament-gold: #f7b21e;
    --ornament-amber: #f59a1c;
    --ink: #1f1f1f;
    --paper: #ffffff;
    --backdrop: #ece8e4;
  }
  * { box-sizing: border-box; margin: 0; padding: 0; }
  html, body {
    width: 1200px; height: 1200px; overflow: hidden;
    background: var(--backdrop);
    font-family: "Roboto Condensed", "Arial Narrow", sans-serif;
  }
  .card {
    position: absolute; left: 278px; width: 663px; height: 376px;
    overflow: hidden;
    box-shadow: 0 3px 8px rgba(0,0,0,0.25);
  }
  .card--front { top: 196px; background: var(--paper); }
  .card--back  { top: 617px; background: var(--brand-orange); }

  .ornament {
    position: absolute; top: 0; right: 0; width: 205px; height: 100%;
    background: radial-gradient(ellipse at 72% 55%, var(--ornament-amber) 0%, var(--ornament-gold) 45%, rgba(247,178,30,0.45) 75%, rgba(247,178,30,0) 100%);
    -webkit-mask-image: linear-gradient(to right, transparent 0%, #000 35%);
    mask-image: linear-gradient(to right, transparent 0%, #000 35%);
  }
  .card--back .ornament {
    background: radial-gradient(ellipse at 72% 55%, var(--ornament-gold) 0%, var(--ornament-amber) 45%, rgba(245,154,28,0.5) 75%, rgba(245,154,28,0) 100%);
  }

  .wordmark {
    position: absolute; display: flex; align-items: center; gap: 10px;
    color: var(--brand-orange); font-size: 42px; line-height: 1; font-weight: 400;
  }
  .wordmark__square { width: 26px; height: 26px; background: var(--brand-orange); }
  .card--front .wordmark { left: 38px; top: 82px; }
  .card--back .wordmark {
    left: 0; width: 458px; top: 150px; justify-content: center;
    color: var(--paper); font-size: 62px;
  }
  .card--back .wordmark__square { width: 36px; height: 36px; background: var(--paper); }

  .services {
    position: absolute; left: 40px; width: 418px; top: 238px;
    text-align: center; color: var(--paper); font-size: 15px; line-height: 21px;
    list-style: none;
  }
  .services__item { display: inline; }
  .services__item + .services__item::before { content: " \2022  "; }

  .person { position: absolute; left: 38px; top: 162px; width: 420px; }
  .person__name { color: var(--brand-orange); font-size: 21px; line-height: 28px; font-weight: 400; white-space: nowrap; }
  .person__role { color: var(--ink); font-size: 17px; line-height: 22px; }

  .contact { position: absolute; left: 38px; top: 250px; list-style: none; }
  .contact__item {
    display: flex; align-items: center; gap: 8px;
    color: var(--ink); font-size: 17px; line-height: 22px;
  }
  .contact__icon { width: 18px; height: 16px; flex: none; }

  .license { position: absolute; left: 38px; top: 330px; font-size: 17px; color: var(--ink); }
  .license__label { color: var(--brand-orange); }
</style>
</head>
<body>

<section class="card card--front" aria-label="Business card front">
  <div class="wordmark"><span class="wordmark__square"></span><span>HomeWise</span></div>

  <div class="person">
    <h1 class="person__name">Danielle Reyes Crawford, OTR/L, CAPS, ECHM</h1>
    <p class="person__role">Occupational Therapist</p>
    <p class="person__role">Home Modification &amp; Accessibility Specialist</p>
  </div>

  <ul class="contact">
    <li class="contact__item">
      <svg class="contact__icon" viewBox="0 0 18 16" aria-hidden="true" fill="none" stroke="#d0802b" stroke-width="1.2">
        <circle cx="9" cy="8" r="7"/><ellipse cx="9" cy="8" rx="3" ry="7"/>
        <line x1="2" y1="8" x2="16" y2="8"/><line x1="3" y1="4.5" x2="15" y2="4.5"/><line x1="3" y1="11.5" x2="15" y2="11.5"/>
      </svg>
      www.homewiseforyears.com
    </li>
    <li class="contact__item">
      <svg class="contact__icon" viewBox="0 0 18 16" aria-hidden="true">
        <rect x="1" y="3" width="16" height="11" fill="#d0802b"/>
        <polyline points="1,3 9,9.5 17,3" fill="none" stroke="#fff" stroke-width="1.3"/>
      </svg>
      homewiseforyears@nestmail.example
    </li>
    <li class="contact__item">
      <svg class="contact__icon" viewBox="0 0 18 16" aria-hidden="true" fill="#d0802b">
        <path d="M1 6 Q9 0 17 6 L15 8 L12 6.5 L12 5 Q9 4 6 5 L6 6.5 L3 8 Z"/>
        <rect x="4" y="8" width="10" height="7" rx="1"/>
        <circle cx="9" cy="11.5" r="1.8" fill="#fff"/>
      </svg>
      (503)218-4057
    </li>
  </ul>

  <p class="license"><span class="license__label">CCB #</span>: 487315</p>

  <div class="ornament" role="img" aria-label="Decorative orange and gold floral swirl ornament with circles"></div>
</section>

<section class="card card--back" aria-label="Business card back">
  <div class="wordmark"><span class="wordmark__square"></span><span>HomeWise</span></div>
  <ul class="services" aria-label="Services offered">
    <li class="services__item">Occupational Therapy</li>
    <li class="services__item">Home Safety &amp; Accessibility Assessments</li>
    <li class="services__item">Home Modification Consulting</li>
    <li class="services__item">Project Management</li>
  </ul>
  <div class="ornament" role="img" aria-label="Decorative orange and gold floral swirl ornament with circles"></div>
</section>

</body>
</html>
```